Report redesign

We need a designer to redesign the attached report and provide us with a template so we can use it for future reports. We want the redesigned report to look like the one in this link:

http://www3.lumatrexa.org/docs/LTX_SCT_RRN_NewModelsAddressingSupplyChainTransportRisk_IndustryAgenda_2012.pdf

Colors
0392cd
3176b5
85acd3
85cae6
33a6d7
0292cd
33b8a4

```html
<!DOCTYPE html>
<html lang="en">
<head>
<meta charset="utf-8">
<title>Biomass Supply Assessment – Report Pages</title>
<link href="https://fonts.googleapis.com/css2?family=Open+Sans:wght@400;600;700&display=swap" rel="stylesheet">
<style>
  :root {
    --cyan: #1fb4dc;
    --cyan-line: #8fd9ec;
    --green: #4fd12e;
    --green-dark: #2e9e1c;
    --text: #3d3d3d;
    --page-border: #d4d4d4;
    --bg: #ffffff;
    --canvas: #ffffff;
  }
  * { box-sizing: border-box; margin: 0; padding: 0; }
  html, body { width: 865px; height: 1200px; overflow: hidden; background: var(--canvas); }
  body { font-family: "Open Sans", Arial, sans-serif; color: var(--text); }
  .sheet { width: 1080px; height: 1500px; position: relative; transform: scale(0.8); transform-origin: 0 0; }
  .page { position: absolute; background: var(--bg); border: 1px solid var(--page-border); overflow: hidden; }
  .page--9  { left: 18px;  top: 22px;  width: 509px; height: 719px; }
  .page--10 { left: 551px; top: 22px;  width: 509px; height: 719px; }
  .page--11 { left: 18px;  top: 760px; width: 513px; height: 725px; }
  .page--12 { left: 551px; top: 760px; width: 509px; height: 725px; }
  .rule { position: absolute; top: 45px; width: 1px; height: 650px; background: var(--cyan-line); }
  .col { position: absolute; font-size: 8.1px; line-height: 11.3px; }
  .col p { margin-bottom: 8px; }
  .section-title { color: var(--cyan); font-size: 12.5px; font-weight: 600; letter-spacing: .1px; margin-bottom: 17px; }
  .sub-title { color: var(--green); font-size: 10px; font-weight: 600; margin: 4px 0 1px; }
  .sub-title--cyan { color: var(--cyan); }
  .accent-cyan { color: var(--cyan); }
  .accent-green { color: var(--green); }
  .footer { position: absolute; bottom: 28px; font-size: 5.6px; color: var(--cyan-line); white-space: nowrap; }
  .footer .num { font-size: 8px; color: var(--cyan); margin-left: 14px; }
  .footnote { position: absolute; font-size: 5.3px; line-height: 7px; color: #666; }
  ol.sources { list-style: none; }
  ol.sources li { position: relative; padding-left: 16px; margin-left: 12px; margin-bottom: 8px; }
  ol.sources li span.n { position: absolute; left: 0; }
  ul.duties { list-style: none; margin: 6px 0 12px 12px; }
  ul.duties li { position: relative; padding: 3px 0 3px 18px; border-bottom: 1px solid var(--cyan-line); }
  ul.duties li::before { content: "-"; position: absolute; left: 0; }
  .map-title { color: var(--cyan); font-size: 10px; font-weight: 600; margin-bottom: 10px; white-space: nowrap; }
  .map { width: 237px; height: 184px; border: 1px solid #ccc;
         background: radial-gradient(ellipse at 60% 70%, #3b8f2a 0%, #6fd13d 35%, #9df05a 60%, #d9e8f0 85%); }
  .table-title { color: var(--cyan); font-size: 9px; font-weight: 600; white-space: nowrap; width: 256px; padding-bottom: 3px; border-bottom: 1px solid var(--cyan-line); margin-bottom: 24px; }
  table.fmu { width: 256px; border-collapse: collapse; font-size: 7px; line-height: 9px; }
  table.fmu caption { color: var(--green); font-weight: 600; font-size: 7.2px; margin-bottom: 3px; }
  table.fmu th { color: var(--green); font-weight: 600; font-size: 5.8px; border: 1px solid var(--cyan-line); padding: 1px 2px; height: 11px; }
  table.fmu td { border-top: 1px solid var(--cyan-line); border-bottom: 1px solid var(--cyan-line); padding: 0 2px; height: 15px; }
  table.fmu td + td { text-align: center; border-left: 1px solid var(--cyan-line); }
  table.fmu td:last-child { border-right: 1px solid var(--cyan-line); }
  table.fmu tr.total td { color: var(--green); }
</style>
</head>
<body>
<div class="sheet">

  <section class="page page--9">
    <div class="col" style="left:30px; top:43px; width:283px;">
      <h2 class="section-title">2.0 WOOD FIBRE CATEGORIES</h2>
      <p>The research team investigated the following categories of wood fibre:</p>
      <h3 class="sub-title">2.1 PULPWOOD</h3>
      <p>Pulpwood is defined as a roundwood product that will be reduced to individual wood fibres by chemical or mechanical means. It has traditionally been used to make paper, paperboard, or oriented strand board. However, recent developments in the renewable energy industry have created new markets for Pulpwood as feedstock for fuel production facilities, especially wood pellets. The moisture content of Pulpwood is typically 45% to 55%, with a calorific value of 4,500 to 5,500 BTU/lb. (as received).</p>
      <h3 class="sub-title">2.2 CLEAN CHIP</h3>
      <p>Clean Chip is defined as wood chip derived from debarked logs. It can be a byproduct of dimensional lumber production, or made directly from debarked and chipped Pulpwood. The market for this category of wood fibre is highly competitive, as it constitutes the primary type of feedstock for pulp and paper mills. The moisture content of Clean Chip is usually between 45% and 50%. The calorific value ranges between 5,000 and 5,500 BTU/lb. (as received).</p>
      <p>There are three separate categories of Clean Chip available in the Collingwood, ON woodshed: Hardwood Clean Chip, Poplar Mill Chip, and Poplar Roundwood Chip. Hardwood Clean Chip is produced as a byproduct of lumber production, and is comprised of a mix of Hardwood species such as maple and oak. Poplar Mill Chip is also produced as a byproduct of lumber production, but is comprised entirely of Poplar wood. Poplar Roundwood Chip, on the other hand, is produced by chip mills that debark and process the entire Poplar log.</p>
      <h3 class="sub-title">2.3 SAWDUST</h3>
      <p>Sawdust is defined as sawmill residual measuring less than 0.1” in size. If Sawdust comes from previously kiln-dried wood, it is considered “dry”. If it comes from non-dried wood, it is referred to as “green”. Sawdust is most commonly used for particleboard and MDF manufacturing, as well as wood pellet feedstock. It is also used for animal bedding, boiler fuel and liquid waste solidification. Sawdust tends to be homogenous in terms of species and moisture content. The moisture content of dry Sawdust is between 8% and 18%, and its calorific value is between 7,000 and 8,500 BTU/lb. (as received). The moisture content of green Sawdust is between 40% and 50%, and its calorific value is between 5,000 and 6,000 BTU/lb. (as received).</p>
      <h3 class="sub-title">2.4 SHAVINGS</h3>
      <p>Shavings are typically defined as sawmill residual measuring between 0.1” and 1” in size. Shavings are a product of planer operations. If Shavings come from previously kiln-dried wood, it is called “dry”. Similarly, if it comes from non-dried wood, it is referred to as “green”. Shavings are utilized by the same manufacturing operations as Sawdust, including animal bedding and feedstock for wood pellet production. The moisture content of dry Shavings is between 8% and 18%, and its calorific value is between 7,000 and 8,500 BTU/lb. (as received). The moisture content of green Shavings is between 40% and 50%, and its calorific value is between 5,000 and 6,000 BTU/lb. (as received).</p>
    </div>
    <div class="rule" style="left:328px;"></div>
    <div class="footer" style="left:325px;">Biomass Supply Assessment – Collingwood, ON <span class="num">9</span></div>
  </section>

  <section class="page page--10">
    <div class="col" style="left:30px; top:40px; width:280px;">
      <h2 class="section-title">3.0 STANDING TIMBER ANALYSIS</h2>
      <p>To understand the environmental as well as supply sustainability of Hardwood fibre resource, it is important to conduct a thorough analysis of standing timber. Fibre supply sustainability analysis is important for two reasons: <span class="accent-cyan">1) it shows that there is a sustainable and long-term supply of fibre,</span> and <span class="accent-cyan">2) it shows that sourcing fibre is environmentally sustainable, and, in fact, benefits forest health.</span> Timber grows constantly, adding millions of tonnes of biomass each year to Ontario’s forest cover. To keep forests healthy, specific quantities of timber ought to be harvested. This section presents an analysis of the availability of standing timber for new fibre consumers, taking account of sustainability and forest health concerns.</p>
      <p>To conduct this analysis, the research team acquired data from two sources:</p>
      <ol class="sources">
        <li><span class="n">1.</span><span class="accent-cyan">Ontario’s Forest Resource Inventory (FRI):</span> The Forest Resources Inventory gathers information about tree species composition, range, age and distribution. The information is collected by the Ontario Ministry of Natural Resources and Forestry (OMN RF). The database includes lands licences to the forest industry, as well as non-licensed areas within Forest Management Units (FMUs), provincial and federal parks, and private lands.</li>
        <li><span class="n">2.</span><span class="accent-cyan">Ontario Available Wood Reports:</span> OMNRF publishes the Ontario Available Wood Report on a monthly basis. The report indicates the projected wood supply by each consumer, and the remaining available wood supply for potential new users. The model used to generate the report averages wood supply over a 10-year period. Therefore, the estimates it provides do not indicate the exact quantity of fibre available now, but rather an average annual availability over a 10-year horizon.</li>
      </ol>
      <h3 class="sub-title">3.1 PUBLIC LANDS</h3>
      <p>Public forest lands, also referred to as Crown forests, are managed by the Ontario Ministry of Natural Resources and Forestry (OMNRF). Specifically, the responsibilities of OMNRF include:</p>
      <ul class="duties">
        <li>Determination of Crown wood supply (available harvest area in approved Forest Management Plans);</li>
        <li>Allocation and licensing of Crown timber and facilities;</li>
        <li>Wood measurement;</li>
        <li>Establishment and administration of Crown timber charges.</li>
      </ul>
      <p>The Crown forests are divided into broad units, called Forest Management Units (FMUs), as seen below in Map 2.</p>
    </div>
    <div class="footnote" style="left:30px; top:674px; width:280px;">(2) Unhealthy forests have a higher risk of catastrophic wildfire occurrence, insect outbreak, and other ecosystem disturbances.</div>
    <div class="rule" style="left:329px;"></div>
    <div class="footer" style="left:320px;">Biomass Supply Assessment – Collingwood, ON <span class="num">10</span></div>
  </section>

  <section class="page page--11">
    <div class="col" style="left:33px; top:40px; width:178px;">
      <h2 class="sub-title" style="margin-bottom:20px;">Forest Management Units</h2>
      <p>The OMNRF divides the province into Forest Management Units (FMUs). The Ministry requires each FMU to have a Forest Management Plan (FMP), which describes forest management practices, including harvestable timber volumes, allowed in each particular FMU. All timber harvesters have to abide by these plans, and therefore all data relevant to timber harvesting is kept at the FMU level. There are 11 FMUs in the woodshed (Map 2 and Table 1). The research team divided these FMUs into three zones based on proximity to Collingwood, ON. Zone 1 contains the Bancroft-Minden, French-Severn, and Algonquin Park FMUs. Zone 2 contains the Mazinaw-Lanark, Ottawa Valley, Nipissing, Sudbury, and Temagami FMUs. Zone 3 contains the Northshore, Spanish, and Timiskaming FMUs.</p>
    </div>
    <div class="rule" style="left:228px;"></div>
    <div class="col" style="left:246px; top:80px; width:240px;">
      <h3 class="map-title">Map 2: Forest Management Units (FMUs) by Zone</h3>
      <div class="map" role="img" aria-label="Map of the woodshed around Collingwood, ON showing Forest Management Units shaded in three green tones by zone"></div>
    </div>
    <div class="footer" style="left:324px;">Biomass Supply Assessment – Collingwood, ON <span class="num">11</span></div>
  </section>

  <section class="page page--12">
    <div class="col" style="left:30px; top:47px; width:276px;">
      <h2 class="sub-title sub-title--cyan" style="margin-bottom:22px;">3.1.1 HARDWOOD SPECIES DISTRIBUTION</h2>
      <p class="accent-green">Forests are composed of two general species groups: Hardwoods and Softwoods. Larchmont can only intake Hardwoods, and is specifically interested in Poplar. Since a large portion of delivered fibre cost is due to trucking costs, and therefore depends on distance travelled, it is important to understand where Hardwoods are located. The more Hardwood roundwood located relatively close to Collingwood, the less Larchmont will pay for Pulpwood. This section presents spatial distribution of Hardwoods by Forest Management Unit.</p>
      <p>Of the total public lands in the woodshed, there are 2.38 million hectares (ha) of productive Hardwood stands . Productive stands are forested lands that could be harvested, i.e. they exclude protected lands. 0.6 million hectares (26%) of all Hardwood stands are Poplar stands.</p>
      <p>Area-wise, FMUs located in Zone 3 are most abundant in Hardwood. In total, there are 1,130,780 hectares of Hardwood forests in Zone 3. Of those, 565,390 ha (50%) are Poplar stands. In Zone 1 two forests are especially abundant in Hardwood: Northshore (282,822 ha) and Algonquin Park (350,652 ha). In total, there are 858,504 ha of Hardwood in Zone 1, of which 309,618 ha (36%) are Poplar stands. Zone 2 has 802,540 ha of Hardwood in total. However, Zone 2 stands are spread over five FMUs, of which only Nipissing FMU has relatively large areas of Hardwood stands: 295,198 hectares. 144,484 ha (18%) of Hardwood stands in Zone 2 are Poplar. Tables 1 and 2 and Maps 3 and 4 show Hardwood distribution in the study area.</p>
      <h3 class="table-title" style="margin-top:26px;">Table 1: Hardwood Distribution in Productive Stands by FMU</h3>
      <table class="fmu">
        <caption>Productive Crown Forest (ha)</caption>
        <thead><tr><th>FMU</th><th>Poplar</th><th>Other Hardwood</th><th>Total</th><th>%Poplar</th></tr></thead>
        <tbody>
          <tr><td>Algonquin Park</td><td>50,677</td><td>299,975</td><td>350,652</td><td>14%</td></tr>
          <tr><td>Bancroft-Minden</td><td>37,501</td><td>47,670</td><td>85,171</td><td>44%</td></tr>
          <tr><td>French-Severn</td><td>65,077</td><td>217,745</td><td>282,822</td><td>23%</td></tr>
          <tr><td>Mazinaw-Lanark</td><td>8,979</td><td>95,228</td><td>104,207</td><td>9%</td></tr>
          <tr><td>Nipissing</td><td>45,215</td><td>249,983</td><td>295,198</td><td>15%</td></tr>
          <tr><td>Northshore</td><td>72,191</td><td>272,283</td><td>344,474</td><td>21%</td></tr>
          <tr><td>Ottawa Valley</td><td>40,794</td><td>102,709</td><td>143,503</td><td>28%</td></tr>
          <tr><td>Spanish</td><td>90,102</td><td>150,511</td><td>240,613</td><td>37%</td></tr>
          <tr><td>Sudbury</td><td>37,986</td><td>114,022</td><td>152,008</td><td>25%</td></tr>
          <tr><td>Temagami</td><td>11,510</td><td>96,114</td><td>107,624</td><td>11%</td></tr>
          <tr><td>Timiskaming</td><td>147,325</td><td>126,092</td><td>273,417</td><td>54%</td></tr>
          <tr class="total"><td>TOTAL</td><td>607,357</td><td>1,772,332</td><td>2,379,689</td><td>26%</td></tr>
        </tbody>
      </table>
    </div>
    <div class="rule" style="left:329px;"></div>
    <div class="col" style="left:349px; top:82px; width:140px;">
      <p>These estimates indicate that, relative to Collingwood, Hardwood stands are distributed with no obvious pattern. For instance, the closely located Algonquin Park FMU (Zone 1) is most abundant in Hardwood timber (area-wise); however, the second most Hardwood abundant FMU is the Northshore forest, located in Zone 3 (Map 3). That said, the pattern emerges in case of Poplar. Area-wise, 51% of Poplar is located in Zone 3. This suggests that in order to source significant quantities of Poplar Pulpwood, Larchmont would likely source the roundwood from Zone 3 FMUs. This conclusion is further confirmed by the projected availability of Poplar roundwood data (Map 7) .</p>
    </div>
    <div class="footnote" style="left:30px; top:678px; width:300px;">(3) A stand refers to a small forest, typically defined by a dominant species.<br>(4) With the exception of the Timiskaming FMU, where no additional Poplar is available for harvest.</div>
    <div class="footer" style="left:320px;">Biomass Supply Assessment – Collingwood, ON <span class="num">12</span></div>
  </section>

</div>
</body>
</html>
```